Business Card of PebbleFinch
PebbleFinch
Bright & Fun-filled
Daniel Osei, CFA
President
412 Whitmore Suite 208
Irvine, CA 92655
daniel@pebblefinch.example
pebblefinch.example

```html
<!DOCTYPE html>
<html lang="en">
<head>
<meta charset="utf-8">
<title>PebbleFinch – Business Card</title>
<link href="https://fonts.googleapis.com/css2?family=Source+Sans+3:wght@400;600;700&display=swap" rel="stylesheet">
<style>
  :root {
    --canvas: #d9d9d9;
    --card-white: #ffffff;
    --brand-red: #e31e26;
    --brand-red-dark: #c8161d;
    --brand-gold: #f4a81d;
    --ink: #3a3a3a;
    --rule: #9a9a9a;
  }
  * { box-sizing: border-box; margin: 0; padding: 0; }
  html, body {
    width: 1200px; height: 901px; overflow: hidden;
    background: var(--canvas);
    font-family: "Source Sans 3", "Segoe UI", sans-serif;
  }
  .stage {
    width: 1200px; height: 901px;
    display: flex; flex-direction: column; align-items: center; justify-content: center;
    gap: 34px;
  }
  .card {
    position: relative; width: 700px; height: 400px; overflow: hidden;
    box-shadow: 0 6px 18px rgba(0,0,0,.18);
  }

  /* Back side */
  .card-back {
    background: var(--brand-red);
    display: flex; flex-direction: column; align-items: center; justify-content: center;
    gap: 22px;
  }
  .back-mark {
    display: flex; align-items: center; gap: 14px;
    color: var(--card-white); font-weight: 700; font-size: 64px; letter-spacing: -0.5px;
  }
  .back-mark .dot { width: 26px; height: 26px; border-radius: 50%; background: var(--card-white); }
  .back-web {
    color: var(--card-white); font-size: 17px; letter-spacing: 3px;
  }

  /* Front side */
  .card-front { background: var(--card-white); }
  .front-logo {
    position: absolute; left: 34px; top: 56px;
    color: var(--brand-gold); font-weight: 700; font-size: 40px; letter-spacing: -0.5px;
  }
  .name-band {
    position: absolute; left: 0; top: 132px; width: 100%; height: 150px;
  }
  .holder {
    position: absolute; left: 34px; top: 146px; color: var(--card-white);
  }
  .holder-name { font-size: 22px; font-weight: 600; line-height: 1.1; }
  .holder-role { font-size: 15px; margin-top: 4px; }
  .corner-mark {
    position: absolute; right: 34px; top: 258px;
    color: var(--brand-gold); font-weight: 700; font-size: 34px; letter-spacing: -0.5px;
  }
  .contact-row {
    position: absolute; left: 34px; right: 20px; bottom: 28px;
    display: flex; align-items: flex-end; color: var(--ink); font-size: 14px; line-height: 1.45;
  }
  .contact-group { padding: 0 12px; border-left: 1px solid var(--rule); }
  .contact-group:first-child { padding-left: 0; border-left: 0; }
  .contact-line { display: flex; align-items: center; gap: 7px; white-space: nowrap; }
  .contact-line svg { width: 14px; height: 14px; flex: none; fill: var(--brand-red); }
</style>
</head>
<body>
<main class="stage">

  <section class="card card-back" aria-label="Business card, back">
    <div class="back-mark"><span class="dot"></span>PebbleFinch</div>
    <div class="back-web">pebblefinch.example</div>
  </section>

  <section class="card card-front" aria-label="Business card, front">
    <div class="front-logo">PebbleFinch</div>

    <svg class="name-band" viewBox="0 0 700 150" preserveAspectRatio="none" aria-hidden="true">
      <rect x="0" y="0" width="700" height="64" fill="var(--brand-red)"/>
      <polygon points="300,64 700,64 700,118" fill="var(--brand-red-dark)"/>
    </svg>

    <div class="holder">
      <div class="holder-name">Daniel Osei, CFA</div>
      <div class="holder-role">President</div>
    </div>

    <div class="corner-mark">PebbleFinch</div>

    <div class="contact-row">
      <div class="contact-group">
        <div>412 Whitmore Suite 208</div>
        <div>Irvine, CA 92655</div>
      </div>
      <div class="contact-group">
        <div class="contact-line">
          <svg viewBox="0 0 16 16"><rect x="4" y="1" width="8" height="14" rx="1.5"/><rect x="5.5" y="3" width="5" height="8" fill="#fff"/></svg>
          714-555-0142
        </div>
        <div class="contact-line">
          <svg viewBox="0 0 16 16"><path d="M3 2h3l1 3-2 1.5a9 9 0 0 0 4.5 4.5L11 9l3 1v3a2 2 0 0 1-2 2A11 11 0 0 1 1 4a2 2 0 0 1 2-2z"/></svg>
          888-555-0176
        </div>
      </div>
      <div class="contact-group">
        <div class="contact-line">
          <svg viewBox="0 0 16 16"><path d="M3 2h3l1 3-2 1.5a9 9 0 0 0 4.5 4.5L11 9l3 1v3a2 2 0 0 1-2 2A11 11 0 0 1 1 4a2 2 0 0 1 2-2z"/></svg>
          888-555-0193
        </div>
        <div class="contact-line">
          <svg viewBox="0 0 16 16"><rect x="1" y="6" width="14" height="8" rx="1"/><rect x="4" y="2" width="8" height="5" fill="none" stroke="var(--brand-red)" stroke-width="1.5"/></svg>
          714-555-0128
        </div>
      </div>
      <div class="contact-group">
        <div class="contact-line">
          <svg viewBox="0 0 16 16"><rect x="1" y="3" width="14" height="10" rx="1"/><path d="M2 4l6 5 6-5" fill="none" stroke="#fff" stroke-width="1.3"/></svg>
          daniel@pebblefinch.example
        </div>
        <div class="contact-line">
          <svg viewBox="0 0 16 16"><circle cx="8" cy="8" r="7"/><path d="M1 8h14M8 1c-3 3-3 11 0 14M8 1c3 3 3 11 0 14" fill="none" stroke="#fff" stroke-width="1"/></svg>
          pebblefinch.example
        </div>
      </div>
    </div>
  </section>

</main>
</body>
</html>
```